Brambleton Chiropractic. We have two locations that we want to advertise on the same card. Kelwin MotionCare campus address: 3815 Tamsey Rd., Suite 240, Flowood, MS 39987. Madison address: 428 Pellham Ct., Building D., Madison, MS 39974. website: www.drbrambleton-example.com. o:(601)555-0147 f:(601)555-0183

Target Market(s)

Health care decision makers: primary care doctors and mothers

Contact Information for Business Card

I have no idea; up for any suggestions and I'd do much better picking from examples versus describing what I'm looking for. We are in a very high end location and would like the cards to look really sharp.

Requirements
Must have
• My name, Marcus L Denbrook, D.C.

```html
<!DOCTYPE html>
<html lang="en">
<head>
<meta charset="utf-8">
<title>Brambleton Chiropractic – Business Card</title>
<link href="https://fonts.googleapis.com/css2?family=Tinos&family=Lato:wght@400&display=swap" rel="stylesheet">
<style>
  :root {
    --backdrop: #2b2b2b;
    --card-black: #030303;
    --card-white: #f1f1f1;
    --ink-light: #f4f4f4;
    --ink-dark: #1a1a1a;
    --shadow: rgba(0,0,0,0.55);
  }
  html, body {
    margin: 0;
    padding: 0;
    width: 1200px;
    height: 960px;
    overflow: hidden;
    background: var(--backdrop);
  }
  .canvas {
    position: relative;
    width: 1200px;
    height: 960px;
  }
  .card {
    position: absolute;
    width: 598px;
    height: 343px;
    box-shadow: 0 4px 10px var(--shadow);
    overflow: hidden;
  }
  .card--front { left: 323px; top: 108px; background: var(--card-white); }
  .card--back  { left: 321px; top: 494px; background: var(--card-black); }

  .front__info {
    position: absolute;
    left: 0; top: 0;
    width: 289px; height: 100%;
    background: var(--card-black);
    color: var(--ink-light);
    font-family: "Tinos", "Times New Roman", serif;
    font-size: 15px;
    line-height: 19.5px;
  }
  .info__name {
    position: absolute;
    left: 27px; top: 61px;
    margin: 0;
    font-size: 18px;
    font-weight: 400;
    letter-spacing: 0.3px;
    text-transform: uppercase;
  }
  .info__address {
    position: absolute;
    left: 27px;
    margin: 0;
    font-style: normal;
  }
  .info__address--flowood { top: 95px; }
  .info__address--madison { top: 158px; }
  .info__contacts {
    position: absolute;
    left: 27px; top: 222px;
    margin: 0; padding: 0;
    list-style: none;
  }
  .info__contacts li {
    display: flex;
    align-items: center;
    gap: 8px;
  }
  .info__contacts svg { width: 13px; height: 13px; fill: var(--ink-light); }

  .front__brand {
    position: absolute;
    left: 289px; top: 0;
    width: 309px; height: 100%;
    display: flex;
    align-items: center;
    justify-content: center;
  }
  .brand-name {
    font-family: "Tinos", "Times New Roman", serif;
    color: var(--ink-dark);
    font-size: 22px;
    line-height: 24px;
    letter-spacing: 1px;
    text-transform: uppercase;
    text-align: left;
  }

  .back__brand {
    position: absolute;
    left: 0; top: 110px;
    width: 100%;
    text-align: center;
    font-family: "Tinos", "Times New Roman", serif;
    color: var(--ink-light);
    font-size: 24px;
    line-height: 30px;
    letter-spacing: 2px;
    text-transform: uppercase;
  }
  .back__url {
    position: absolute;
    left: 0; top: 278px;
    width: 100%;
    text-align: center;
    font-family: "Lato", "Helvetica", sans-serif;
    color: var(--ink-light);
    font-size: 15px;
    letter-spacing: 4.5px;
    text-transform: uppercase;
  }
</style>
</head>
<body>
<main class="canvas">

  <section class="card card--front" aria-label="Business card front">
    <div class="front__info">
      <h1 class="info__name">Marcus L Denbrook, D.C.</h1>
      <address class="info__address info__address--flowood">
        Kelwin MotionCare campus :<br>
        3815 Tamsey Rd., Suite 240<br>
        Flowood, MS 39987.
      </address>
      <address class="info__address info__address--madison">
        Madison address:<br>
        428 Pellham Ct., Building D.<br>
        Madison, MS 39974.
      </address>
      <ul class="info__contacts">
        <li>
          <svg viewBox="0 0 16 16" aria-label="Phone"><path d="M1 5c0-2 2-3 7-3s7 1 7 3v1h-4V4.5H5V6H1zM3 7h10l1 7H2zm5 1.5a2.2 2.2 0 1 0 0 4.4 2.2 2.2 0 0 0 0-4.4z"/></svg>
          (601)555-0147
        </li>
        <li>
          <svg viewBox="0 0 16 16" aria-label="Fax"><path d="M4 1h8v5H4zM1 7h14v7H1zm2 2v1h4V9zm0 2v1h4v-1z"/></svg>
          (601)555-0183
        </li>
        <li>
          <svg viewBox="0 0 16 16" aria-label="Website"><path d="M8 1a7 7 0 1 0 0 14A7 7 0 0 0 8 1zm-1 2.5c1 .5 2 .2 2.5 1S8 6 7 6.5 5 8 6 9.5s3 .5 3.5 2-1 2-1.5 2C5 13 3 11 3 8c0-2 1.5-4 4-4.5z"/></svg>
          www.drbrambleton-example.com
        </li>
      </ul>
    </div>
    <div class="front__brand">
      <div class="brand-name">Brambleton<br>Chiropractic</div>
    </div>
  </section>

  <section class="card card--back" aria-label="Business card back">
    <div class="back__brand">Brambleton<br>Chiropractic</div>
    <div class="back__url">www.drbrambleton-example.com</div>
  </section>

</main>
</body>
</html>
```